Harbourlight Dental Centre Kellmoor business cards and presentation folder

dental practice needing innovative black business cards for 2 different dentists witrh appointment details written at the back of the card for the patient.
name of dentists: Dr Priyanka R Venkataraman B.D.S., M.P.H (Melb)
Dr. Tom Kadle B.D.S.

Target Market(s)

professioinal, working class

Industry/Entity Type

Dental Clinic

Contact Information for Business Card

Dr. Tom Kadle B.D.S.

Font styles to use
Sans Serif

Requirements
Must have
• Front side: logo
• dentist name
• phone number: 07- 5481 2937
• back side: appointment details: date, time,
• Address: 117C, 58 Tarrow Street, Kellmoor - 4871, Eastmerra
• Email: admin@harbourlightdentalcentrekellmoor.com.au
• Website: www.harbourlightdentalcentre.com.au
• preferable logo colors
Nice to have
• classy look more pleasing

```html
<!DOCTYPE html>
<html lang="en">
<head>
<meta charset="utf-8">
<title>Harbourlight Dental Centre – Business Card</title>
<link href="https://fonts.googleapis.com/css2?family=Arimo:wght@400;700&family=Open+Sans:ital,wght@0,400;0,600;1,400&display=swap" rel="stylesheet">
<style>
  :root {
    --backdrop: #5b4a3b;
    --card-dark: #221f20;
    --accent: #a7c981;
    --accent-soft: #9fbf7b;
    --accent-edge: #c9dcb2;
    --rule: #9a9a9a;
    --text-light: #d6d6d6;
    --text-dark: #5a5a5a;
    --dots: #8a8a8a;
    --paper: #ffffff;
    --note: #c4c4c4;
  }
  * { margin: 0; padding: 0; box-sizing: border-box; }
  html, body { width: 1200px; height: 987px; overflow: hidden; }
  body { background: var(--backdrop); position: relative; font-family: "Arimo", Arial, sans-serif; }

  .card { position: absolute; left: 293px; width: 615px; height: 351px; background: var(--card-dark); overflow: hidden; }
  .card--front { top: 130px; }
  .card--back { top: 505px; }

  .brand { position: absolute; display: flex; align-items: center; gap: 10px; color: var(--accent); font-family: "Arimo", Arial, sans-serif; font-weight: 700; letter-spacing: 0.3px; white-space: nowrap; }
  .brand__dot { width: 14px; height: 14px; border-radius: 50%; background: var(--accent); flex: none; }
  .card--front .brand { left: 32px; top: 68px; font-size: 25px; }
  .card--back .brand { right: 32px; top: 34px; font-size: 19px; }

  .dentists { position: absolute; left: 31px; top: 184px; color: var(--accent); font-weight: 700; }
  .dentist { font-size: 21px; line-height: 27px; white-space: nowrap; }
  .dentist__quals { font-size: 16px; }

  .divider { position: absolute; left: 31px; top: 242px; width: 555px; height: 1px; background: var(--rule); }

  .contacts { position: absolute; left: 31px; top: 251px; list-style: none; color: var(--text-light); font-size: 15px; }
  .contacts li { display: flex; align-items: center; gap: 6px; height: 23.5px; white-space: nowrap; }
  .contacts svg { width: 15px; height: 15px; flex: none; }

  .address { position: absolute; right: 29px; top: 252px; text-align: right; color: var(--text-light); font-size: 15px; line-height: 20.5px; font-style: normal; white-space: nowrap; }

  .band { position: absolute; left: 0; right: 0; bottom: 0; height: 14px; background: var(--accent-soft); border-top: 2px solid var(--accent-edge); }

  .back__header { position: absolute; left: 0; top: 0; width: 100%; height: 95px; }
  .back__title { position: absolute; left: 33px; top: 34px; font-family: "Open Sans", Arial, sans-serif; font-weight: 600; font-size: 19px; color: var(--accent); letter-spacing: 0.2px; }

  .appointments { position: absolute; left: 0; top: 95px; width: 100%; height: 219px; background: var(--paper); list-style: none; font-family: "Open Sans", Arial, sans-serif; font-size: 16px; color: var(--text-dark); padding-top: 24px; }
  .appointment { display: flex; align-items: baseline; height: 49.5px; padding: 0 30px 0 31px; white-space: nowrap; }
  .appointment__fill { border-bottom: 2px dotted var(--dots); height: 1px; margin: 0 2px 0 6px; }
  .appointment__fill--date { width: 232px; }
  .appointment__fill--time { width: 150px; margin-right: 10px; }

  .policy { position: absolute; left: 0; bottom: 0; width: 100%; height: 37px; line-height: 37px; text-align: center; font-family: "Open Sans", Arial, sans-serif; font-style: italic; font-size: 14px; color: var(--note); }
</style>
</head>
<body>

<section class="card card--front" aria-label="Business card front">
  <div class="brand"><span class="brand__dot"></span>Harbourlight Dental Centre</div>

  <div class="dentists">
    <p class="dentist">Dr Priyanka R Venkataraman <span class="dentist__quals">B.D.S., M.P.H (Melb)</span></p>
    <p class="dentist">Dr. Tom Kadle <span class="dentist__quals">B.D.S.</span></p>
  </div>

  <div class="divider"></div>

  <ul class="contacts">
    <li>
      <svg viewBox="0 0 16 16" aria-hidden="true"><path fill="#d6d6d6" d="M2 6c0-2 2-3 6-3s6 1 6 3v1h-3V5.5H5V7H2zM4 8h8l1.5 5h-11zM8 9.2a1.6 1.6 0 1 0 0 3.2 1.6 1.6 0 0 0 0-3.2z"/></svg>
      07- 5481 2937
    </li>
    <li>
      <svg viewBox="0 0 16 16" aria-hidden="true"><rect x="1.5" y="3.5" width="13" height="9" fill="#d6d6d6"/><path d="M1.5 4l6.5 5 6.5-5" fill="none" stroke="#221f20" stroke-width="1.2"/></svg>
      admin@harbourlightdentalcentrekellmoor.com.au
    </li>
    <li>
      <svg viewBox="0 0 16 16" aria-hidden="true"><circle cx="8" cy="8" r="6.5" fill="#d6d6d6"/><path d="M5 4.5c1 .5 1.5 1.5 1 2.5s-2 1-2 2.5M9 3c0 1.5 2 1.5 2.5 3s-1 2-1 3.5 1 2 1.5 2.5" fill="none" stroke="#221f20" stroke-width="1.3"/></svg>
      www.harbourlightdentalcentre.com.au
    </li>
  </ul>

  <address class="address">117C, 58 Tarrow Street<br>Kellmoor - 4871<br>Eastmerra</address>

  <div class="band"></div>
</section>

<section class="card card--back" aria-label="Business card back">
  <header class="back__header">
    <h2 class="back__title">NEXT APPOINTMENT</h2>
    <div class="brand"><span class="brand__dot"></span>Harbourlight Dental Centre</div>
  </header>

  <ul class="appointments">
    <li class="appointment">Date :<span class="appointment__fill appointment__fill--date"></span>Time :<span class="appointment__fill appointment__fill--time"></span>AM/BM</li>
    <li class="appointment">Date :<span class="appointment__fill appointment__fill--date"></span>Time :<span class="appointment__fill appointment__fill--time"></span>AM/BM</li>
    <li class="appointment">Date :<span class="appointment__fill appointment__fill--date"></span>Time :<span class="appointment__fill appointment__fill--time"></span>AM/BM</li>
    <li class="appointment">Date :<span class="appointment__fill appointment__fill--date"></span>Time :<span class="appointment__fill appointment__fill--time"></span>AM/BM</li>
  </ul>

  <p class="policy">Please give 48 hours notice cancelling your appointment or a fee may be charged</p>
</section>

</body>
</html>
```